New Business Card Design for Business Consulting Business

We need a business card design that reflects the simplicity of our business. We partner with our clients to help them deliver change. We are a different kind of business consulting group. We don't just provide you with the theory. We provide you with the leadership and capability to execute change.

Vendora is a professional services organisation that partners with their clients to lead the execution of strategic process and system improvement initiatives. Vendora combines hands on delivery with coaching in best practice methodologies and approaches to build their clients capabilities to ensure their ongoing success in project implementations. Vendora offers business advisory services in Project Management, Business Process Management, Change Management and Business Analytics.

Reason: Hi Designers, Thanks for all of your great designs. There are some really creative and cool ideas. Everyone is really capturing the essence of my business Vendora. I am extending the deadline for the business card design by 6 days as I need to consult my Marketing colleague who won't be back in Australia until Wednesday. I would like to sit down with them and review all of the best designs. The key themes of the things I have really liked on my first review are: 1) Capturing the company website on the back of the card. 2) Including the company logo on the back of the card too. 3) Including the types of services on the back of the card that the company offers - Project Management - Business Process Management - Change Management - Business Analytics 4) Utilising some images on the back of the card Just so everyone knows the colour palette for the Vendora company logo is: R: 0 G: 86 B: 162 or C: 97% M: 73% Y: 4% K: 0% Thanks Gerald

Hi Designers,

Thanks for all of your submissions to date.  I am working through each design and will provide feedback on all the great work.

One thing I would like to ask is if you could submit a version that has my academic credentials under or after my name.  I am not a big fan of doing this but as I am in business consulting it does seem to be quite common.

I hold a Bachelor of Commerce (BCom) and a Master of Business Administration (MBA)

Thanks

Gerald

Hi Designers,

Thanks for all of your fantastic designs.  There are some really great designs here for my business.  I am still in the process of reviewing designs and should have this completed by tomorrow.  Some of the things I have learnt from this round of designs are:

1) I prefer to have the card without my academic qualifications

2) I really like cards that have a blue back

3) I prefer to have my name and title either left or right of centre

I hope this helps and I will endeavour to get through all of the designs tomorrow

Cheers

Gerald

Target Market(s)

We target large corporate organisations

Industry/Entity Type

Leadership

Requirements
Must have
• Must have the following business details

Gerald Huxton - Director
Address: Level 7, 82 Fernhill Road, Melbourne, Australia, 3000
Phone: +61 3 527 481 903
Fax: +61 3 9254 3718
Email: gerald.huxton@vendora-example.com.au
LinkedIn: au.linkedin.com/in/geraldphuxton/
Twiiter: @geraldphuxton
Website: www.vendora-example.com.au

```html
<!DOCTYPE html>
<html lang="en">
<head>
<meta charset="utf-8">
<title>Vendora Business Card</title>
<link rel="stylesheet" href="https://fonts.googleapis.com/css2?family=Open+Sans:wght@300;400;600&display=swap">
<style>
  :root {
    --brand-blue: #0056a2;
    --backdrop: #3a332e;
    --card-white: #ffffff;
    --stripe-1: #4a4a4a;
    --stripe-2: #5c5c5c;
    --stripe-3: #6e6e6e;
    --stripe-4: #808080;
    --stripe-5: #939393;
    --stripe-6: #a3a3a3;
    --icon-tile: #3b3b3b;
    --ink: #333333;
    --ink-soft: #555555;
  }
  * { margin: 0; padding: 0; box-sizing: border-box; }
  html, body { width: 1200px; height: 569px; overflow: hidden; }
  body {
    background: var(--backdrop);
    font-family: "Open Sans", Arial, sans-serif;
    position: relative;
  }
  .card {
    position: absolute;
    top: 114px;
    width: 540px;
    height: 330px;
    overflow: hidden;
    box-shadow: 0 10px 30px rgba(0,0,0,0.45);
  }
  .card--back { left: 620px; background: var(--brand-blue); }
  .card--front { left: 40px; background: var(--card-white); }

  /* back */
  .back-wordmark {
    position: absolute;
    left: 0; right: 0; top: 118px;
    text-align: center;
    color: var(--card-white);
    font-weight: 300;
    font-size: 76px;
    letter-spacing: 2px;
    line-height: 1;
  }

  /* front */
  .front-band {
    position: absolute;
    left: 0; top: 0;
    width: 100%; height: 120px;
    background: var(--brand-blue);
  }
  .front-logo {
    position: absolute;
    right: 28px; top: 18px;
    display: flex;
    align-items: center;
    gap: 12px;
  }
  .front-logo__name {
    color: var(--card-white);
    font-weight: 300;
    font-size: 60px;
    letter-spacing: 2px;
    line-height: 1;
  }
  .front-logo__dot {
    width: 56px; height: 56px;
    border-radius: 50%;
    background: var(--card-white);
  }
  .front-logo__suffix {
    position: absolute;
    right: 96px; top: 94px;
    color: var(--card-white);
    font-size: 10px;
    letter-spacing: 1px;
    line-height: 1;
  }

  .contact-list {
    position: absolute;
    left: 0; top: 120px;
    width: 300px;
    list-style: none;
  }
  .contact-row {
    height: 26px;
    margin-bottom: 2px;
    display: flex;
    justify-content: flex-end;
    align-items: center;
    color: var(--card-white);
    font-size: 10.5px;
  }
  .contact-row:nth-child(1) { background: var(--stripe-1); }
  .contact-row:nth-child(2) { background: var(--stripe-2); }
  .contact-row:nth-child(3) { background: var(--stripe-3); }
  .contact-row:nth-child(4) { background: var(--stripe-4); }
  .contact-row:nth-child(5) { background: var(--stripe-5); }
  .contact-row:nth-child(6) { background: var(--stripe-6); }
  .contact-row__text { padding-right: 8px; white-space: nowrap; }
  .contact-row__icon {
    width: 26px; height: 26px;
    background: var(--icon-tile);
    display: flex; align-items: center; justify-content: center;
  }
  .contact-row__icon--plain { background: var(--brand-blue); }

  .profile {
    position: absolute;
    left: 318px; top: 150px;
    width: 200px;
    text-align: center;
    color: var(--ink);
  }
  .profile__name { font-size: 18px; font-weight: 400; }
  .profile__title { font-size: 11px; color: var(--ink-soft); margin-top: 1px; }
  .profile__address {
    margin-top: 26px;
    font-size: 12px;
    line-height: 1.45;
    color: var(--ink);
    text-align: left;
    padding-left: 12px;
  }
</style>
</head>
<body>

<section class="card card--back" aria-label="Card back">
  <div class="back-wordmark">Vendora</div>
</section>

<section class="card card--front" aria-label="Card front">
  <div class="front-band"></div>
  <div class="front-logo">
    <span class="front-logo__name">Vendora</span>
    <span class="front-logo__dot"></span>
  </div>
  <span class="front-logo__suffix">Pty Ltd</span>

  <ul class="contact-list">
    <li class="contact-row"></li>
    <li class="contact-row">
      <span class="contact-row__text">+61 3 527 481 903</span>
      <span class="contact-row__icon">
        <svg width="14" height="14" viewBox="0 0 24 24"><path fill="#fff" d="M6.6 10.8a15.1 15.1 0 0 0 6.6 6.6l2.2-2.2c.3-.3.7-.4 1-.2 1.1.4 2.3.6 3.6.6.6 0 1 .4 1 1V20c0 .6-.4 1-1 1A17 17 0 0 1 3 4c0-.6.4-1 1-1h3.5c.6 0 1 .4 1 1 0 1.3.2 2.5.6 3.6.1.3 0 .7-.2 1z"/></svg>
      </span>
    </li>
    <li class="contact-row">
      <span class="contact-row__text">gerald.huxton@vendora-example.com.au</span>
      <span class="contact-row__icon">
        <svg width="14" height="14" viewBox="0 0 24 24"><rect x="3" y="6" width="18" height="12" fill="none" stroke="#fff" stroke-width="2"/><path d="M3 6l9 7 9-7" fill="none" stroke="#fff" stroke-width="2"/></svg>
      </span>
    </li>
    <li class="contact-row">
      <span class="contact-row__text">www.vendora-example.com.au</span>
      <span class="contact-row__icon">
        <svg width="14" height="14" viewBox="0 0 24 24" fill="none" stroke="#fff" stroke-width="1.8"><circle cx="12" cy="12" r="9"/><ellipse cx="12" cy="12" rx="4" ry="9"/><path d="M3 12h18"/></svg>
      </span>
    </li>
    <li class="contact-row">
      <span class="contact-row__text">social.example/geraldphuxton</span>
      <span class="contact-row__icon contact-row__icon--plain"></span>
    </li>
    <li class="contact-row">
      <span class="contact-row__text">profile.example/in/geraldphuxton</span>
      <span class="contact-row__icon contact-row__icon--plain"></span>
    </li>
  </ul>

  <div class="profile">
    <div class="profile__name">Gerald Huxton</div>
    <div class="profile__title">Director</div>
    <div class="profile__address">Level 7, 82 Fernhill Road<br>Melbourne, Australia, 3000</div>
  </div>
</section>

</body>
</html>
```